Road Construction Company needs business cards

We would like a new business card designed for our business.

We're a road construction company based in Qld, Australia.

Can the business card please have the following information on it.

Name: Brent Malvoy
Position: General Manager
Phone: 0471 592 304
Email: Brent.malvoy@quendix.com.au
Address: 87 Harrowgate Ave, Pindarra, QLD, 4000
Website: www.quendix.com.au

Visually we'd like the card to be professional and simple.

Attached is our logo.

Our website is www.quendix.com.au

Target Market(s)

Men aged 25-60

Contact Information for Business Card

As listed in project description

Font styles to use
Serif

Requirements
Must have
• Large logo on back of card

```html
<!DOCTYPE html>
<html lang="en">
<head>
<meta charset="utf-8">
<title>Quendix Business Card</title>
<link href="https://fonts.googleapis.com/css2?family=Poppins:wght@400;500;700&display=swap" rel="stylesheet">
<style>
  :root {
    --page-bg: #cbd8dd;
    --navy-deep: #1c355f;
    --navy: #123f72;
    --blue: #08538e;
    --stripe: #0a5a9c;
    --sky: #1fa7d6;
    --sky-soft: #34a6d8;
    --white: #ffffff;
    --ink: #1a1a1a;
  }
  * { margin: 0; padding: 0; box-sizing: border-box; }
  html, body { width: 1200px; height: 1200px; overflow: hidden; }
  body {
    background: var(--page-bg);
    font-family: "Poppins", sans-serif;
    display: flex;
    flex-direction: column;
    align-items: center;
    justify-content: center;
    gap: 56px;
  }
  .card {
    position: relative;
    width: 900px;
    height: 514px;
    border-radius: 48px;
    overflow: hidden;
    background: var(--white);
  }
  .card-art { position: absolute; inset: 0; width: 100%; height: 100%; }
  .brand-name {
    position: absolute;
    color: var(--white);
    font-weight: 700;
    letter-spacing: 0.02em;
    line-height: 1;
  }
  .card-front .brand-name {
    left: 0; right: 0; top: 50%;
    transform: translateY(-50%);
    text-align: center;
    font-size: 104px;
  }
  .card-back .brand-name {
    left: 70px; top: 100px;
    font-size: 50px;
  }
  .contact-block {
    position: absolute;
    left: 466px;
    top: 190px;
    color: var(--ink);
  }
  .person-name { font-size: 34px; font-weight: 500; line-height: 1.15; }
  .person-role { font-size: 21px; font-weight: 400; margin-bottom: 22px; }
  .contact-list { list-style: none; }
  .contact-item {
    display: flex;
    align-items: center;
    gap: 12px;
    font-size: 20px;
    line-height: 1;
    margin-bottom: 16px;
  }
  .contact-icon { width: 20px; height: 20px; flex: none; fill: var(--sky); }
</style>
</head>
<body>

  <section class="card card-front">
    <svg class="card-art" viewBox="0 0 900 514" preserveAspectRatio="none" aria-hidden="true">
      <defs>
        <linearGradient id="frontNavy" x1="0" y1="1" x2="1" y2="0">
          <stop offset="0" stop-color="#1c355f"/>
          <stop offset="1" stop-color="#07548f"/>
        </linearGradient>
      </defs>
      <rect width="900" height="514" fill="url(#frontNavy)"/>
      <polygon points="0,0 280,0 0,270" fill="var(--sky)"/>
      <polygon points="0,300 290,20 300,20 0,315" fill="var(--stripe)" opacity="0.55"/>
      <polygon points="0,340 330,20 336,20 0,346" fill="var(--stripe)" opacity="0.6"/>
      <polygon points="900,260 900,266 640,514 634,514" fill="var(--stripe)"/>
      <polygon points="900,220 900,230 600,514 590,514" fill="var(--stripe)" opacity="0.5"/>
      <polygon points="900,320 900,514 700,514" fill="var(--white)"/>
    </svg>
    <div class="brand-name">QUENDIX</div>
  </section>

  <section class="card card-back">
    <svg class="card-art" viewBox="0 0 900 514" preserveAspectRatio="none" aria-hidden="true">
      <defs>
        <linearGradient id="backNavy" x1="0" y1="0" x2="0" y2="1">
          <stop offset="0" stop-color="#1c355f"/>
          <stop offset="1" stop-color="#08538e"/>
        </linearGradient>
      </defs>
      <rect width="900" height="514" fill="var(--white)"/>
      <polygon points="0,0 560,0 92,514 0,514" fill="url(#backNavy)"/>
      <polygon points="520,0 542,0 74,514 52,514" fill="var(--stripe)"/>
      <polygon points="310,340 530,514 126,514" fill="var(--sky-soft)"/>
    </svg>
    <div class="brand-name">QUENDIX</div>

    <div class="contact-block">
      <h1 class="person-name">Brent Malvoy</h1>
      <p class="person-role">General Manager</p>
      <ul class="contact-list">
        <li class="contact-item">
          <svg class="contact-icon" viewBox="0 0 24 24" aria-hidden="true"><path d="M6.6 10.8a15.2 15.2 0 0 0 6.6 6.6l2.2-2.2a1 1 0 0 1 1-.25 11.4 11.4 0 0 0 3.6.57 1 1 0 0 1 1 1V20a1 1 0 0 1-1 1A17 17 0 0 1 3 4a1 1 0 0 1 1-1h3.5a1 1 0 0 1 1 1 11.4 11.4 0 0 0 .57 3.6 1 1 0 0 1-.25 1z"/></svg>
          <span>0471 592 304</span>
        </li>
        <li class="contact-item">
          <svg class="contact-icon" viewBox="0 0 24 24" aria-hidden="true"><path d="M2 5h20v14H2z M2 5l10 8 10-8" fill="var(--sky)" stroke="var(--white)" stroke-width="1.6"/></svg>
          <span>Brent.malvoy@quendix.com.au</span>
        </li>
        <li class="contact-item">
          <svg class="contact-icon" viewBox="0 0 24 24" aria-hidden="true"><path d="M12 2a7 7 0 0 0-7 7c0 5 7 13 7 13s7-8 7-13a7 7 0 0 0-7-7zm0 9.5A2.5 2.5 0 1 1 12 6.5a2.5 2.5 0 0 1 0 5z"/></svg>
          <span>87 Harrowgate Ave, Pindarra, QLD, 4000</span>
        </li>
        <li class="contact-item">
          <svg class="contact-icon" viewBox="0 0 24 24" aria-hidden="true"><circle cx="12" cy="12" r="10"/><path d="M2 12h20M12 2c3 3 3 17 0 20M12 2c-3 3-3 17 0 20" fill="none" stroke="var(--white)" stroke-width="1.5"/></svg>
          <span>Website: www.quendix.com.au</span>
        </li>
      </ul>
    </div>
  </section>

</body>
</html>
```